Commercial Loan Originator Business Card (CHANGE COLORS SCHEME)

CHANGE COLOR SCHEME - SAME DESIGN

Name Marissa Lantham
Title Commercial Loan Originator
Office (800) 641-2905 x68
Direct (240) 617-2435
Email brightleaf4you@mailpost.example

Name Derek Fallow
Office (800) 641-2905 x70
Direct (410) 932-1864
Email d.falthebroker@mailpost.example

Name Gordon Wexley
Office (800) 641-2905 x71
Direct (215) 346-2081
Email g.wexley37@mailpost.example

Name Lyn Moreau
Office (800) 641-2905 x
Direct (202) 458-1937
Email lmoreau64@mailpost.example

Name Nadia Strand
Office (800) 641-2905 x72
Direct (240) 871-5246
Email qrzhomelending@mailpost.example

```html
<!DOCTYPE html>
<html lang="en">
<head>
<meta charset="utf-8">
<title>Commercial Loan Originator Business Cards</title>
<link href="https://fonts.googleapis.com/css2?family=Montserrat:wght@500;700&display=swap" rel="stylesheet">
<style>
  :root {
    --backdrop: #e4e7ec;
    --card: #15243d;
    --card-edge: #2a3d5e;
    --ink: #ffffff;
    --ink-soft: #d5dbe6;
    --accent: #d0a85c;
    --photo-a: #3f5a82;
    --photo-b: #27395a;
  }
  * { margin: 0; padding: 0; box-sizing: border-box; }
  html, body {
    width: 1200px; height: 1047px; overflow: hidden;
    background: var(--backdrop);
  }
  .card-sheet {
    display: grid;
    grid-template-columns: repeat(2, 560px);
    grid-auto-rows: 306px;
    gap: 30px;
    justify-content: center;
    padding-top: 34px;
  }
  .business-card {
    position: relative;
    background: var(--card);
    border: 2px solid var(--card-edge);
    border-radius: 16px;
    box-shadow: 0 8px 22px rgba(20, 30, 50, 0.22);
    font-family: "Montserrat", sans-serif;
    color: var(--ink);
  }
  .business-card:last-child { grid-column: 1 / span 2; justify-self: center; width: 560px; }
  .holder-name {
    position: absolute; left: 27px; top: 63px;
    font-size: 22px; font-weight: 700; letter-spacing: 0.3px;
    text-transform: uppercase; white-space: nowrap;
  }
  .holder-title {
    position: absolute; left: 27px; top: 98px;
    font-size: 12.5px; font-weight: 500; color: var(--accent);
  }
  .contact-list {
    position: absolute; left: 27px; top: 166px;
    list-style: none;
  }
  .contact-item {
    display: flex; align-items: center; gap: 7px;
    height: 22px;
    font-size: 12.5px; font-weight: 500; color: var(--ink-soft);
    white-space: nowrap;
  }
  .contact-icon { width: 13px; height: 13px; fill: var(--accent); flex: none; }
  .icon-line { fill: none; stroke: var(--accent); stroke-width: 1.8; stroke-linejoin: round; }
  .icon-fold { fill: none; stroke: var(--card); stroke-width: 2; }
  .portrait {
    position: absolute; left: 343px; top: 60px;
    width: 192px; height: 192px; border-radius: 50%;
    background: radial-gradient(circle at 50% 35%, var(--photo-a) 0 30%, var(--photo-b) 100%);
    border: 2px solid var(--accent);
  }
</style>
</head>
<body>
<main class="card-sheet">

  <article class="business-card">
    <h1 class="holder-name">Marissa Lantham</h1>
    <p class="holder-title">Commercial Loan Originator</p>
    <ul class="contact-list">
      <li class="contact-item"><svg class="contact-icon" viewBox="0 0 24 24" aria-hidden="true"><path d="M3 9c0-3 4-5 9-5s9 2 9 5v2h-5V9c0-1-2-1.5-4-1.5S8 8 8 9v2H3zM6 13h12l2 7H4z"/></svg><span>(800) 641-2905 x68</span></li>
      <li class="contact-item"><svg class="contact-icon" viewBox="0 0 24 24" aria-hidden="true"><path class="icon-line" d="M22 2 2 10l7 3 2 8 3-5 5 3zM9 13l10-9-7 11z"/></svg><span>(240) 617-2435</span></li>
      <li class="contact-item"><svg class="contact-icon" viewBox="0 0 24 24" aria-hidden="true"><path d="M2 5h20v14H2z"/><path class="icon-fold" d="M2 5l10 8 10-8"/></svg><span>brightleaf4you@mailpost.example</span></li>
    </ul>
    <div class="portrait" role="img" aria-label="Round portrait photo of Marissa Lantham"></div>
  </article>

  <article class="business-card">
    <h1 class="holder-name">Derek Fallow</h1>
    <p class="holder-title">Commercial Loan Originator</p>
    <ul class="contact-list">
      <li class="contact-item"><svg class="contact-icon" viewBox="0 0 24 24" aria-hidden="true"><path d="M3 9c0-3 4-5 9-5s9 2 9 5v2h-5V9c0-1-2-1.5-4-1.5S8 8 8 9v2H3zM6 13h12l2 7H4z"/></svg><span>(800) 641-2905 x70</span></li>
      <li class="contact-item"><svg class="contact-icon" viewBox="0 0 24 24" aria-hidden="true"><path class="icon-line" d="M22 2 2 10l7 3 2 8 3-5 5 3zM9 13l10-9-7 11z"/></svg><span>(410) 932-1864</span></li>
      <li class="contact-item"><svg class="contact-icon" viewBox="0 0 24 24" aria-hidden="true"><path d="M2 5h20v14H2z"/><path class="icon-fold" d="M2 5l10 8 10-8"/></svg><span>d.falthebroker@mailpost.example</span></li>
    </ul>
    <div class="portrait" role="img" aria-label="Round portrait photo of Derek Fallow"></div>
  </article>

  <article class="business-card">
    <h1 class="holder-name">Gordon Wexley</h1>
    <p class="holder-title">Commercial Loan Originator</p>
    <ul class="contact-list">
      <li class="contact-item"><svg class="contact-icon" viewBox="0 0 24 24" aria-hidden="true"><path d="M3 9c0-3 4-5 9-5s9 2 9 5v2h-5V9c0-1-2-1.5-4-1.5S8 8 8 9v2H3zM6 13h12l2 7H4z"/></svg><span>(800) 641-2905 x71</span></li>
      <li class="contact-item"><svg class="contact-icon" viewBox="0 0 24 24" aria-hidden="true"><path class="icon-line" d="M22 2 2 10l7 3 2 8 3-5 5 3zM9 13l10-9-7 11z"/></svg><span>(215) 346-2081</span></li>
      <li class="contact-item"><svg class="contact-icon" viewBox="0 0 24 24" aria-hidden="true"><path d="M2 5h20v14H2z"/><path class="icon-fold" d="M2 5l10 8 10-8"/></svg><span>g.wexley37@mailpost.example</span></li>
    </ul>
    <div class="portrait" role="img" aria-label="Round portrait photo of Gordon Wexley"></div>
  </article>

  <article class="business-card">
    <h1 class="holder-name">Lyn Moreau</h1>
    <p class="holder-title">Commercial Loan Originator</p>
    <ul class="contact-list">
      <li class="contact-item"><svg class="contact-icon" viewBox="0 0 24 24" aria-hidden="true"><path d="M3 9c0-3 4-5 9-5s9 2 9 5v2h-5V9c0-1-2-1.5-4-1.5S8 8 8 9v2H3zM6 13h12l2 7H4z"/></svg><span>(800) 641-2905 x</span></li>
      <li class="contact-item"><svg class="contact-icon" viewBox="0 0 24 24" aria-hidden="true"><path class="icon-line" d="M22 2 2 10l7 3 2 8 3-5 5 3zM9 13l10-9-7 11z"/></svg><span>(202) 458-1937</span></li>
      <li class="contact-item"><svg class="contact-icon" viewBox="0 0 24 24" aria-hidden="true"><path d="M2 5h20v14H2z"/><path class="icon-fold" d="M2 5l10 8 10-8"/></svg><span>lmoreau64@mailpost.example</span></li>
    </ul>
    <div class="portrait" role="img" aria-label="Round portrait photo of Lyn Moreau"></div>
  </article>

  <article class="business-card">
    <h1 class="holder-name">Nadia Strand</h1>
    <p class="holder-title">Commercial Loan Originator</p>
    <ul class="contact-list">
      <li class="contact-item"><svg class="contact-icon" viewBox="0 0 24 24" aria-hidden="true"><path d="M3 9c0-3 4-5 9-5s9 2 9 5v2h-5V9c0-1-2-1.5-4-1.5S8 8 8 9v2H3zM6 13h12l2 7H4z"/></svg><span>(800) 641-2905 x72</span></li>
      <li class="contact-item"><svg class="contact-icon" viewBox="0 0 24 24" aria-hidden="true"><path class="icon-line" d="M22 2 2 10l7 3 2 8 3-5 5 3zM9 13l10-9-7 11z"/></svg><span>(240) 871-5246</span></li>
      <li class="contact-item"><svg class="contact-icon" viewBox="0 0 24 24" aria-hidden="true"><path d="M2 5h20v14H2z"/><path class="icon-fold" d="M2 5l10 8 10-8"/></svg><span>qrzhomelending@mailpost.example</span></li>
    </ul>
    <div class="portrait" role="img" aria-label="Round portrait photo of Nadia Strand"></div>
  </article>

</main>
</body>
</html>
```